Create a pouch design for a new sports supplement product

Dimensions are 235mm (width) x 335mm (length) x 110mm (gusset)
File 1 - Extension of design brief please read both briefs
File 2 - Is 2 potential pouches this is just to give you a better example of size the dimensions are for the pouch on the right. This picture is not to give you design ideas as I am not very keen on either of these designs.
We need a design to be printed onto the pouches of our whey protein product. The brand name is 'Brisk Fuelworks' and needs to be displayed on the packaging either just writing or a simple logo design. I am not the most creative person in the world but have put together a more detailed brief listing some of the key information that needs to be included on the pouch (See attachment) Please feel free if you have experience of this the sports supplement market or have different ideas then please feel free to explore them.
The pouch would either be printed straight onto the pouch, or possibly just a printed label (front & back) to be stuck onto the pouch. Please design either or both.
Open to different colour schemes. Design has to be modern looking and eye-catching.
Some key points;
High quality whey protein concentrate
All Natural
Soy free
Great tasting
Please google image search 'protein pouches' to see other designs if your not familiar with the sports supplement market.
Any questions feel free to ask.
Updates
Project Deadline Extended
Reason: give me chance to give feedback
Hi, Thanks for all your design! I am really busy at the moment so haven't had chance to give feedback and have a proper look through all the designs. I have extended the time frame to give myself chance to give proper feedback and see any changes needed. Expect feedback sunday at the latest, and I will be pick a design early next week.
Target Market(s)
Sports supplement market. Product is a whey protein shake
Industry/Entity Type
Nutrition
Look and feel
Each slider illustrates characteristics of the customer's brand and the style your logo design should communicate.

```html
<!DOCTYPE html>
<html lang="en">
<head>
<meta charset="utf-8">
<title>Brisk Fuelworks – Natural Whey Protein Pouch Front</title>
<link rel="stylesheet" href="https://fonts.googleapis.com/css2?family=Archivo:ital,wght@0,700;0,900;1,700;1,900&family=Archivo+Narrow:wght@500;700&display=swap">
<style>
  :root {
    --pouch-orange: #e5522c;
    --pouch-orange-deep: #d7432a;
    --pouch-orange-light: #f07a4a;
    --leaf-tint: #f3a887;
    --brand-red: #e4141f;
    --ink: #111111;
    --paper: #ffffff;
    --silver-light: #fbfbfb;
    --silver-dark: #b9b9b9;
    --shadow-brown: #5a2416;
    --stage: #ffffff;
  }
  * { margin: 0; padding: 0; box-sizing: border-box; }
  html, body {
    width: 1200px; height: 814px; overflow: hidden;
    background: var(--stage);
  }
  .pouch-front {
    position: absolute; left: 315px; top: 0;
    width: 570px; height: 814px; overflow: hidden;
    background: linear-gradient(160deg, var(--pouch-orange) 0%, var(--pouch-orange-deep) 100%);
    font-family: "Archivo", Arial, sans-serif;
  }
  .pouch-shapes { position: absolute; inset: 0; }
  .leaf-branch {
    position: absolute; left: 40px; top: 585px; width: 340px; height: 229px;
    background: radial-gradient(ellipse at 40% 55%, rgba(243,168,135,.75), rgba(243,168,135,0) 70%);
  }
  .reseal-tag {
    position: absolute; left: 350px; top: 95px; width: 148px; height: 20px;
    border: 1px dashed #7a2a18; border-radius: 3px;
    font: 500 13px/18px "Archivo Narrow", Arial, sans-serif; color: var(--ink); text-align: center;
  }
  .reseal-tag span { color: var(--paper); }
  .brand-name {
    position: absolute; left: 70px; top: 168px; width: 230px;
    font: 900 34px/1 "Archivo", Arial, sans-serif; color: var(--paper);
    letter-spacing: -0.5px;
  }
  .pack-weight {
    position: absolute; left: 363px; top: 160px; width: 120px; text-align: center;
    font: 900 26px/1 "Archivo", Arial, sans-serif; color: var(--brand-red);
  }
  .pack-servings {
    position: absolute; left: 363px; top: 204px; width: 120px; text-align: center;
    font: 900 30px/1 "Archivo", Arial, sans-serif; color: var(--paper);
  }
  .pack-servings small { display: block; font-size: 13px; margin-top: 3px; }
  .product-natural {
    position: absolute; left: 80px; top: 268px;
    font: italic 900 66px/1 "Archivo", Arial, sans-serif; color: var(--brand-red);
    -webkit-text-stroke: 2px var(--ink); letter-spacing: -1px;
  }
  .product-whey {
    position: absolute; left: 66px; top: 340px;
    font: 900 42px/1 "Archivo", Arial, sans-serif; color: var(--brand-red);
    -webkit-text-stroke: 1.5px var(--ink); transform: rotate(-4deg); transform-origin: left center;
  }
  .flavour-pill {
    position: absolute; left: 122px; top: 403px; width: 200px; height: 30px;
    border: 2px solid var(--ink); border-radius: 15px; background: var(--paper);
    font: italic 900 14px/26px "Archivo", Arial, sans-serif; color: var(--brand-red); text-align: center;
  }
  .benefit-box {
    position: absolute; left: 80px; top: 455px; width: 256px; height: 102px;
    background: var(--paper); border: 3px solid var(--ink); padding: 6px 0 0 26px;
  }
  .benefit-box .benefit-lead { font: italic 900 21px/1 "Archivo", Arial, sans-serif; color: var(--ink); }
  .benefit-box .benefit-red { font: italic 900 13px/1.1 "Archivo", Arial, sans-serif; color: var(--brand-red); }
  .benefit-box .benefit-figure { font: italic 900 18px/1 "Archivo", Arial, sans-serif; color: var(--ink); margin-top: 8px; display: flex; align-items: center; gap: 4px; }
  .benefit-box .benefit-figure small { font-size: 8px; line-height: 1; font-style: normal; }
  .no-artificial {
    position: absolute; left: 340px; top: 400px; width: 176px; height: 176px;
    text-align: center; color: var(--paper); padding-top: 34px;
  }
  .no-artificial .no-word { font: 900 50px/1 "Archivo", Arial, sans-serif; }
  .no-artificial .no-sub { font: italic 700 20px/1.1 "Archivo", Arial, sans-serif; margin-top: 4px; }
  .soy-free {
    position: absolute; left: 370px; top: 563px; width: 110px; height: 110px;
    display: flex; align-items: center; justify-content: center; text-align: center;
    font: 900 23px/1 "Archivo", Arial, sans-serif; color: var(--brand-red);
  }
</style>
</head>
<body>
<main class="pouch-front">
  <svg class="pouch-shapes" width="570" height="814" viewBox="0 0 570 814" aria-hidden="true">
    <defs>
      <linearGradient id="silver" x1="0" y1="0" x2="0" y2="1">
        <stop offset="0" stop-color="var(--silver-light)"/>
        <stop offset=".55" stop-color="#e4e4e4"/>
        <stop offset="1" stop-color="var(--silver-dark)"/>
      </linearGradient>
      <clipPath id="lower-half"><rect x="-90" y="-8" width="180" height="100"/></clipPath>
    </defs>
    <!-- soft swoosh -->
    <path d="M0 40 C160 20 330 80 470 260 L570 330 L570 250 C430 60 240 -10 0 0 Z" fill="var(--pouch-orange-light)" opacity=".35"/>
    <!-- banner arrow shadow and banner -->
    <path d="M54 276 H438 V252 L506 348 L438 444 V420 H54 Z" fill="var(--shadow-brown)" opacity=".55"/>
    <path d="M68 262 H452 V238 L520 334 L452 430 V406 H68 Z" fill="url(#silver)" stroke="#8d8d8d" stroke-width="1"/>
    <!-- starburst -->
    <g transform="translate(423 200)">
      <polygon fill="var(--paper)" stroke="var(--ink)" stroke-width="2" points="76,0 60.8,12.1 70.2,29.1 51.5,34.5 53.7,53.7 34.5,51.5 29.1,70.2 12.1,60.8 0,76 -12.1,60.8 -29.1,70.2 -34.5,51.5 -53.7,53.7 -51.5,34.5 -70.2,29.1 -60.8,12.1 -76,0 -60.8,-12.1 -70.2,-29.1 -51.5,-34.5 -53.7,-53.7 -34.5,-51.5 -29.1,-70.2 -12.1,-60.8 0,-76 12.1,-60.8 29.1,-70.2 34.5,-51.5 53.7,-53.7 51.5,-34.5 70.2,-29.1 60.8,-12.1"/>
      <polygon clip-path="url(#lower-half)" transform="scale(.9)" fill="var(--ink)" points="76,0 60.8,12.1 70.2,29.1 51.5,34.5 53.7,53.7 34.5,51.5 29.1,70.2 12.1,60.8 0,76 -12.1,60.8 -29.1,70.2 -34.5,51.5 -53.7,53.7 -51.5,34.5 -70.2,29.1 -60.8,12.1 -76,0 -60.8,-12.1 -70.2,-29.1 -51.5,-34.5 -53.7,-53.7 -34.5,-51.5 -29.1,-70.2 -12.1,-60.8 0,-76 12.1,-60.8 29.1,-70.2 34.5,-51.5 53.7,-53.7 51.5,-34.5 70.2,-29.1 60.8,-12.1"/>
    </g>
    <!-- no artificial flavours roundel -->
    <circle cx="428" cy="488" r="88" fill="var(--paper)" stroke="var(--ink)" stroke-width="3"/>
    <circle cx="428" cy="488" r="79" fill="var(--ink)"/>
    <!-- soy free roundel -->
    <circle cx="425" cy="618" r="55" fill="var(--paper)" stroke="var(--ink)" stroke-width="4"/>
  </svg>

  <div class="leaf-branch" role="img" aria-label="Pale leafy branch silhouette decoration"></div>

  <div class="reseal-tag">Tear here &amp; <span>Reseal</span></div>
  <div class="brand-name">Brisk Fuelworks</div>

  <div class="pack-weight">909 G</div>
  <div class="pack-servings">30<small>SERVINGS</small></div>

  <h1 class="product-natural">Natural</h1>
  <h2 class="product-whey">WHEY PROTEIN</h2>
  <div class="flavour-pill">STRAWBERRY FLAVOUR</div>

  <div class="benefit-box">
    <p class="benefit-lead">EXCELLENT</p>
    <p class="benefit-red">AMINO ACID PROFILE</p>
    <p class="benefit-figure">80% <small>HIGH<br>QUALITY</small></p>
    <p class="benefit-red">PROTEIN CONTENT</p>
  </div>

  <div class="no-artificial">
    <p class="no-word">NO</p>
    <p class="no-sub">Artificial<br>Flavours</p>
  </div>

  <div class="soy-free">SOY<br>FREE</div>
</main>
</body>
</html>
```